Business Card for a finance professional

I need a business card design to introduce myself to a professional networking (mainly banks) and potential companies to hire and remember me. I would like to use black, grey, white and maybe gold/silver colors and maybe something with my initials(R L F P T). The final design should communicate seriousness, profissionalism and something innovative.

The basic informations in the card are: Name, e-mail, phone number and trabnet. (I'm thinking to put some directly short link to my trabnet account or maybe some app - non QR Code - to add my contacts to a phone directly.)

My name is Mariana Lopes Ferreira Pinto dos Reis (I prefer to use only 'Mariana Lopes' or 'Mariana Reis' but i'm open to other suggestions) and I have 26 years old (just if it helps to build based in my age).
Updates

Dear designers, I wish to thank your participation in this project! It was very difficult to choose one! Thank your for your work! Best regards and success. Mariana

Target Market(s)

Potential hires and big companies.

Industry/Entity Type

Finance

Requirements
Must have
• The informations required at the business card are:
Name: Mariana Lopes F. P. dos Reis
Email: mariana.lop.reis@quellomail.com
Phone: +55 61 8493 5710
TrabNet: http://br.trabnet-perfis.com/in/marianalr/
Nice to have
• Modern and innovative look.
I suggest to use the colors black, grey, white, gold and/or silver, but I'm open to other colors.
Should not have
• A message showing that I need to be hired. It's more to "know me and remember me" than "hire me please".

```html
<!DOCTYPE html>
<html lang="en">
<head>
<meta charset="utf-8">
<title>Mariana Lopes — Business Card</title>
<link rel="stylesheet" href="https://fonts.googleapis.com/css2?family=Cinzel:wght@500&family=Source+Sans+3:wght@400&display=swap">
<style>
  :root {
    --backdrop: #cde8e0;
    --coral-top: #f67472;
    --coral-bottom: #f35756;
    --paper: #ffffff;
    --mark-grey: #7f7f7f;
    --ink: #111111;
    --shadow: rgba(40, 80, 70, 0.18);
  }
  html, body {
    margin: 0;
    padding: 0;
    overflow: hidden;
  }
  .canvas {
    width: 1200px;
    height: 856px;
    background: var(--backdrop);
    display: flex;
    align-items: center;
    justify-content: center;
    gap: 60px;
    overflow: hidden;
  }
  .card {
    position: relative;
    width: 520px;
    height: 297px;
    border-radius: 28px;
    box-shadow: 0 10px 30px var(--shadow);
    overflow: hidden;
  }
  .card--front {
    background: linear-gradient(180deg, var(--coral-top), var(--coral-bottom));
  }
  .card--back {
    background: var(--paper);
  }
  .monogram-disc {
    position: absolute;
    display: block;
  }
  .card--front .monogram-disc {
    left: 190px;
    top: 28px;
    width: 140px;
    height: 140px;
  }
  .card--back .monogram-disc {
    left: 300px;
    top: 38px;
    width: 170px;
    height: 170px;
  }
  .brand {
    position: absolute;
    left: 0;
    right: 0;
    top: 186px;
    margin: 0;
    text-align: center;
    font-family: "Cinzel", serif;
    font-weight: 500;
    color: var(--ink);
    line-height: 1.15;
  }
  .brand__initials {
    display: block;
    font-size: 30px;
    letter-spacing: 12px;
    padding-left: 12px;
  }
  .brand__line {
    display: block;
    font-size: 24px;
    letter-spacing: 4px;
    padding-left: 4px;
  }
  .holder {
    position: absolute;
    left: 30px;
    top: 58px;
    margin: 0;
    font-family: "Source Sans 3", sans-serif;
    font-weight: 400;
    font-size: 24px;
    line-height: 1.0;
    color: var(--ink);
  }
  .holder span {
    display: block;
  }
  .contact {
    position: absolute;
    left: 62px;
    top: 196px;
    margin: 0;
    padding: 0;
    list-style: none;
    font-family: "Source Sans 3", sans-serif;
    font-size: 13px;
    line-height: 1.6;
    color: var(--ink);
  }
</style>
</head>
<body>
  <main class="canvas">
    <section class="card card--front" aria-label="Card front">
      <svg class="monogram-disc" viewBox="0 0 100 100" aria-hidden="true">
        <circle cx="50" cy="50" r="50" fill="var(--mark-grey)"/>
      </svg>
      <h1 class="brand">
        <span class="brand__initials">R L F P T</span>
        <span class="brand__line">BANKS</span>
      </h1>
    </section>

    <section class="card card--back" aria-label="Card back">
      <h2 class="holder">
        <span>Mariana Lopes</span>
        <span>Ferreira</span>
        <span>Pinto</span>
        <span>dos Reis</span>
      </h2>
      <ul class="contact">
        <li>e-mail,</li>
        <li>phone number</li>
        <li>trabnet.</li>
      </ul>
      <svg class="monogram-disc" viewBox="0 0 100 100" aria-hidden="true">
        <circle cx="50" cy="50" r="50" fill="var(--mark-grey)"/>
      </svg>
    </section>
  </main>
</body>
</html>
```